VelaCure Wellness Business Cards

I am looking to have luxury business cards made for my IV Therapy and Wellness business.
Updates

Target Market(s)

Health and Wellness professionals

Industry/Entity Type

MedSpa

Contact Information for Business Card

Tobin Haverly, MSN, RN, CCRN Tobin@velacurewellness.com (916) 582-3179 QR code to website www.velacurewellness.com

```html
<!DOCTYPE html>
<html lang="en">
<head>
<meta charset="UTF-8">
<title>VelaCure Wellness Business Cards</title>
<link href="https://fonts.googleapis.com/css2?family=Montserrat:wght@400;500;600;700&display=swap" rel="stylesheet">
<style>
  :root{
    --navy:#383a85;
    --sky:#3fb8e6;
    --white:#ffffff;
    --ink:#2e2f45;
    --backdrop:#dfe5ee;
  }
  *{margin:0;padding:0;box-sizing:border-box}
  html,body{width:1200px;height:800px;overflow:hidden}
  body{background:var(--backdrop);font-family:'Montserrat',sans-serif;position:relative}
  .card{position:absolute;top:245px;width:540px;height:309px;overflow:hidden;box-shadow:0 6px 18px rgba(30,40,80,.18)}
  .card-front{left:40px;background:var(--white)}
  .card-back{left:620px;background:var(--navy)}
  .front-shapes{position:absolute;inset:0}
  .holder-name{position:absolute;left:58px;top:72px;font-size:22px;font-weight:700;color:var(--navy);letter-spacing:.5px;text-transform:uppercase}
  .holder-title{position:absolute;left:58px;top:102px;font-size:13px;font-weight:500;color:var(--sky)}
  .contact-list{position:absolute;left:48px;top:172px;list-style:none}
  .contact-item{display:flex;align-items:center;height:21px;font-size:12px;font-weight:500;color:var(--ink)}
  .contact-icon{width:18px;height:18px;margin-right:8px;flex:none}
  .website{position:absolute;left:150px;top:279px;font-size:12px;font-weight:500;color:var(--white);letter-spacing:.3px}
  .brand-front{position:absolute;right:34px;top:76px;font-size:20px;font-weight:700;color:var(--navy)}
  .brand-back{position:absolute;left:0;right:0;top:132px;text-align:center;font-size:34px;font-weight:700;color:var(--white)}
</style>
</head>
<body>
  <section class="card card-front">
    <svg class="front-shapes" viewBox="0 0 540 309" width="540" height="309" aria-hidden="true">
      <line x1="42" y1="70" x2="42" y2="168" stroke="var(--sky)" stroke-width="1.5"/>
      <polygon points="318,234 540,106 540,120 338,244" fill="var(--sky)"/>
      <polygon points="0,262 298,262 344,254 540,141 540,309 0,309" fill="var(--navy)"/>
    </svg>
    <div class="holder-name">Tobin Haverly</div>
    <div class="holder-title">CEO &amp; Co-Founder</div>
    <ul class="contact-list">
      <li class="contact-item">
        <svg class="contact-icon" viewBox="0 0 18 18"><circle cx="9" cy="9" r="9" fill="var(--sky)"/><rect x="6.2" y="4" width="5.6" height="10" rx="1" fill="none" stroke="var(--white)" stroke-width="1.2"/><circle cx="9" cy="12.3" r=".6" fill="var(--white)"/></svg>
        +1 408 XXX XXXX
      </li>
      <li class="contact-item">
        <svg class="contact-icon" viewBox="0 0 18 18"><circle cx="9" cy="9" r="9" fill="var(--sky)"/><path d="M6 4.5l1.8 2.3-1 1.2c.7 1.4 1.8 2.5 3.2 3.2l1.2-1 2.3 1.8-1 1.5C9 13.3 4.7 9 4.5 5.5z" fill="var(--white)"/></svg>
        (916) 582-3179
      </li>
      <li class="contact-item">
        <svg class="contact-icon" viewBox="0 0 18 18"><circle cx="9" cy="9" r="9" fill="var(--sky)"/><rect x="4.5" y="5.8" width="9" height="6.4" fill="none" stroke="var(--white)" stroke-width="1.1"/><path d="M4.5 5.8L9 9.6l4.5-3.8" fill="none" stroke="var(--white)" stroke-width="1.1"/></svg>
        Tobin@velacurewellness.com
      </li>
      <li class="contact-item">
        <svg class="contact-icon" viewBox="0 0 18 18"><circle cx="9" cy="9" r="9" fill="var(--sky)"/><path d="M9 14s-3.6-3.7-3.6-6.3a3.6 3.6 0 017.2 0C12.6 10.3 9 14 9 14z" fill="var(--white)"/><circle cx="9" cy="7.7" r="1.3" fill="var(--sky)"/></svg>
        xxxxx 42 Lindell Ave, Ca
      </li>
    </ul>
    <div class="website">www.velacurewellness.com</div>
    <div class="brand-front">VelaCure Wellness</div>
  </section>

  <section class="card card-back">
    <div class="brand-back">VelaCure Wellness</div>
  </section>
</body>
</html>
```